Business Cards and Stationery for Mortgage Company
Mortgage Company
Use same font as used in my logo
Dale Harmon
Branch Manager
24390 Halden Park, Suite210
Irvine, CA 92614
855-442-1739 x4187
dale@kblending.com
www.kestrabaylending.com / www.ratehourlive.com
NMLS#58214 / Broker #04591372
would like to have this information on the project.
www.kestrabaylending.com &
www.ratehourlive.com

```html
<!DOCTYPE html>
<html lang="en">
<head>
<meta charset="utf-8">
<title>Kestra Bay Lending – Stationery</title>
<link href="https://fonts.googleapis.com/css2?family=Cinzel:wght@600&family=Open+Sans:wght@400;600&display=swap" rel="stylesheet">
<style>
:root{
  --stage:#2a2b2e;
  --paper:#ffffff;
  --ink:#2c2f36;
  --muted:#7a8089;
  --blue:#1d6fc4;
  --blue-deep:#0b2f5e;
  --navy:#0a1428;
  --faint:#eef1f5;
  --rule:#c9ced6;
}
*{box-sizing:border-box;margin:0;padding:0}
html,body{width:1200px;height:427px;overflow:hidden;background:var(--stage)}
body{position:relative;font-family:"Open Sans",Arial,sans-serif;color:var(--ink)}
.piece{position:absolute;background:var(--paper);overflow:hidden;box-shadow:0 2px 6px rgba(0,0,0,.45)}
.brand{display:flex;align-items:center;gap:5px;font-family:"Cinzel",Georgia,serif;font-weight:600;color:var(--blue-deep);text-transform:uppercase;letter-spacing:.5px;line-height:1}
.brand .dot{border-radius:50%;background:var(--blue);flex:none}
.swoosh{position:absolute;left:0;bottom:0;width:100%}
.small{font-size:5px;line-height:1.5;color:var(--muted)}
.faint-mark{position:absolute;border-radius:50%;background:var(--faint)}

/* business card front */
.card-front{left:19px;top:158px;width:264px;height:118px}
.card-front .brand{position:absolute;left:12px;top:12px;font-size:11px}
.card-front .brand .dot{width:16px;height:16px}
.card-front .person{position:absolute;right:50px;top:48px;text-align:left}
.card-front .person b{display:block;font-size:7px;color:var(--ink);font-weight:600}
.card-front .person span{font-size:5px;color:var(--muted)}
.card-front .contact{position:absolute;left:12px;top:44px}

/* business card back */
.card-back{left:19px;top:288px;width:264px;height:118px;background:radial-gradient(ellipse at 40% 40%,#27598f 0%,var(--blue-deep) 45%,var(--navy) 100%)}
.card-back .brand{position:absolute;left:40px;top:44px;font-size:12px;color:#fff}
.card-back .brand .dot{width:22px;height:22px;background:#fff}
.card-back .web{position:absolute;left:12px;bottom:8px;font-size:5px;color:#b9c8dc}

/* letterhead */
.letterhead{left:307px;top:34px;width:209px;height:362px}
.letterhead .brand{position:absolute;left:12px;top:12px;font-size:9px}
.letterhead .brand .dot{width:14px;height:14px}
.letterhead .faint-mark{left:30px;top:80px;width:150px;height:150px}
.letterhead .footer{position:absolute;left:12px;right:12px;bottom:30px;display:flex;justify-content:space-between}

/* fax */
.fax{left:533px;top:34px;width:211px;height:362px}
.fax .faint-mark{left:30px;top:80px;width:150px;height:150px}
.fax h1{position:absolute;right:12px;top:12px;font-size:10px;font-weight:600;letter-spacing:1px}
.fax .fields{position:absolute;left:12px;right:12px;top:30px;display:grid;grid-template-columns:1fr 1fr;column-gap:8px;row-gap:4px}
.fax .field{font-size:4.5px;color:var(--ink);border-bottom:.6px solid var(--rule);padding-bottom:1px}
.fax .checks{position:absolute;left:12px;right:12px;top:90px;display:flex;justify-content:space-between;font-size:4px;color:var(--ink)}
.fax .checks span::before{content:"";display:inline-block;width:4px;height:4px;border:.6px solid var(--ink);margin-right:2px;vertical-align:-1px}
.fax .footer{position:absolute;left:12px;right:12px;bottom:30px;display:flex;justify-content:space-between}

/* envelopes */
.env-front{left:840px;top:36px;width:288px;height:144px}
.env-front .brand{position:absolute;left:50%;top:12px;transform:translateX(-50%);font-size:8px}
.env-front .brand .dot{width:14px;height:14px}

.env-back{left:780px;top:216px;width:396px;height:84px;background:var(--paper)}
.env-back svg{position:absolute;inset:0}
.env-back .seal{position:absolute;left:50%;top:44px;transform:translateX(-50%);width:18px;height:18px;border-radius:50%;background:var(--paper);border:2px solid var(--blue)}

.env-window{left:792px;top:306px;width:384px;height:100px}
.env-window .brand{position:absolute;left:12px;top:10px;font-size:9px}
.env-window .brand .dot{width:14px;height:14px}
.env-window .return{position:absolute;left:12px;top:30px}
</style>
</head>
<body>

<!-- business card front -->
<section class="piece card-front">
  <div class="brand"><span class="dot"></span>Kestra Bay Lending</div>
  <div class="contact small">
    24390 Halden Park, Suite210<br>Irvine, CA 92614<br>P: 855-442-1739 x4187<br>dale@kblending.com<br>NMLS#58214 / Broker #04591372
  </div>
  <div class="person"><b>Dale Harmon</b><span>Branch Manager</span></div>
  <svg class="swoosh" viewBox="0 0 264 40" height="40" preserveAspectRatio="none">
    <path d="M0 40 L0 34 Q150 30 264 4 L264 40 Z" fill="var(--blue-deep)"/>
    <path d="M0 34 Q150 30 264 4 L264 10 Q150 34 0 37 Z" fill="var(--blue)"/>
  </svg>
</section>

<!-- business card back -->
<section class="piece card-back">
  <div class="brand"><span class="dot"></span>Kestra Bay Lending</div>
  <div class="web">www.kestrabaylending.com &nbsp;|&nbsp; www.ratehourlive.com</div>
</section>

<!-- letterhead -->
<section class="piece letterhead">
  <div class="brand"><span class="dot"></span>Kestra Bay Lending</div>
  <div class="faint-mark"></div>
  <div class="footer small">
    <div>24390 Halden Park, Suite210<br>Irvine, CA 92614</div>
    <div>P: 855-442-1739 x4187<br>dale@kblending.com</div>
    <div>www.kestrabaylending.com<br>www.ratehourlive.com</div>
  </div>
  <svg class="swoosh" viewBox="0 0 209 26" height="26" preserveAspectRatio="none">
    <path d="M0 26 L0 20 Q120 18 209 2 L209 26 Z" fill="var(--blue-deep)"/>
    <path d="M0 20 Q120 18 209 2 L209 7 Q120 22 0 23 Z" fill="var(--blue)"/>
  </svg>
</section>

<!-- fax cover -->
<section class="piece fax">
  <div class="faint-mark"></div>
  <h1>FAX</h1>
  <div class="fields">
    <div class="field">To:</div><div class="field">From:</div>
    <div class="field">Fax:</div><div class="field">Pages:</div>
    <div class="field">Phone:</div><div class="field">Date:</div>
    <div class="field">Re:</div><div class="field">CC:</div>
  </div>
  <div class="checks">
    <span>Urgent</span><span>For review</span><span>Please comment</span><span>Please reply</span><span>Please recycle</span>
  </div>
  <div class="footer small">
    <div>24390 Halden Park, Suite210<br>Irvine, CA 92614</div>
    <div>P: 855-442-1739 x4187<br>dale@kblending.com</div>
    <div>www.kestrabaylending.com<br>www.ratehourlive.com</div>
  </div>
  <svg class="swoosh" viewBox="0 0 211 26" height="26" preserveAspectRatio="none">
    <path d="M0 26 L0 20 Q120 18 211 2 L211 26 Z" fill="var(--blue-deep)"/>
    <path d="M0 20 Q120 18 211 2 L211 7 Q120 22 0 23 Z" fill="var(--blue)"/>
  </svg>
</section>

<!-- envelope front -->
<section class="piece env-front">
  <div class="brand"><span class="dot"></span>Kestra Bay Lending</div>
</section>

<!-- envelope back with flap -->
<section class="piece env-back">
  <svg viewBox="0 0 396 84" preserveAspectRatio="none">
    <path d="M0 0 L396 0 L396 6 Q200 70 0 6 Z" fill="var(--navy)"/>
    <path d="M0 6 Q200 70 396 6 L396 12 Q200 76 0 12 Z" fill="var(--blue)"/>
  </svg>
  <div class="seal"></div>
</section>

<!-- envelope with return address -->
<section class="piece env-window">
  <div class="brand"><span class="dot"></span>Kestra Bay Lending</div>
  <div class="return small">24390 Halden Park, Suite210<br>Irvine, CA 92614</div>
  <svg class="swoosh" viewBox="0 0 384 20" height="20" preserveAspectRatio="none">
    <path d="M0 20 L0 16 Q220 14 384 2 L384 20 Z" fill="var(--blue-deep)"/>
    <path d="M0 16 Q220 14 384 2 L384 6 Q220 18 0 18 Z" fill="var(--blue)"/>
  </svg>
</section>

</body>
</html>
```